Software as a Service to manage Home Care Management

We need a web site designed for Home Care Management Software as a Service product, that facilitates Home Care organizations to manage and schedule carers to visit client homes. We want a modern look and feel using our existing logo.

Target Market(s)

Home Care Management organizations. Product is similar to: https://kelvantro.co/

Coding

Coded - Design and coding required

Number of Pages Required

3 page

```html
<!DOCTYPE html>
<html lang="en">
<head>
<meta charset="utf-8">
<title>Carelume – Home Care Management</title>
<link href="https://fonts.googleapis.com/css2?family=Merriweather:wght@400;700&display=swap" rel="stylesheet">
<style>
  :root{
    --pink:#f24d89;
    --ice:#cfe6ea;
    --ice-deep:#b9dae0;
    --ink:#1d1d1d;
    --panel:#2d2d2d;
    --white:#ffffff;
    --muted:#555555;
  }
  *{box-sizing:border-box;margin:0;padding:0}
  html,body{width:1200px;height:3888px;overflow:hidden}
  body{position:relative;background:var(--white);font-family:"Merriweather",Georgia,serif;color:var(--ink)}
  .abs{position:absolute}
  .placeholder{position:absolute}

  /* header + hero */
  .hero-bg{left:0;top:0;width:672px;height:912px;background:linear-gradient(160deg,var(--ice),var(--ice-deep))}
  .brand{left:40px;top:20px;display:flex;align-items:center;gap:14px}
  .brand-dot{width:44px;height:44px;border-radius:50%;background:var(--pink)}
  .brand-name{font-size:34px;font-weight:700;color:var(--panel);line-height:1}
  .nav{left:520px;top:0;width:680px;height:88px;background:var(--pink);display:flex;align-items:center;justify-content:flex-end;gap:54px;padding-right:40px}
  .nav a{color:var(--white);text-decoration:none;font-size:18px}
  .nav .login{background:var(--white);color:var(--pink);padding:6px 22px;font-size:17px}
  .hero-title{left:64px;top:196px;width:460px;font-size:40px;line-height:54px;font-weight:700}
  .hero-text{left:64px;top:404px;width:420px;font-size:27px;line-height:40px}
  .btn{left:64px;top:688px;width:216px;height:72px;background:var(--pink);color:var(--white);font-size:20px;font-weight:700;display:flex;align-items:center;justify-content:center}
  .frame{background:var(--white);padding:14px;box-shadow:0 6px 18px rgba(0,0,0,.25)}
  .hero-photo{left:540px;top:152px;width:548px;height:620px}

  /* features */
  .features-head{left:0;top:928px;width:672px;height:80px;background:var(--ice)}
  .features-head h2,.services-head h2{font-size:38px;font-weight:400;position:absolute;top:16px}
  .features-head h2{right:0;left:372px}
  .features-band{left:0;top:1020px;width:1200px;height:520px;background:var(--pink)}
  .features-photo{left:40px;top:1160px;width:608px;height:448px;z-index:2}
  .feature-list{left:752px;top:1088px;list-style:none}
  .feature-list li{color:var(--white);font-size:15px;font-weight:700;line-height:60px}

  /* testimonial */
  .quote-band{left:0;top:1540px;width:1200px;height:800px;background:linear-gradient(135deg,#3a3431,#6e6560 55%,#2e2a28)}
  .quote{left:200px;top:1732px;width:800px;text-align:center;color:var(--white);font-size:42px;line-height:64px;font-weight:700}
  .dots{left:560px;top:2292px;display:flex;gap:14px}
  .dots span{width:14px;height:14px;border-radius:50%;background:rgba(255,255,255,.5)}
  .dots span.on{background:var(--white);width:22px;border-radius:7px}

  /* services */
  .services-bg{left:0;top:2340px;width:1200px;height:720px;background:linear-gradient(160deg,var(--ice),var(--ice-deep))}
  .services-head{left:480px;top:2352px;width:720px;height:80px;background:var(--pink)}
  .services-head h2{left:64px;color:var(--white)}
  .card{top:2500px;width:256px;height:420px;background:var(--white);box-shadow:0 4px 12px rgba(0,0,0,.2);padding:12px}
  .card .card-photo{position:relative;width:232px;height:160px}
  .card h3{font-size:26px;font-weight:700;margin:34px 0 12px 12px}
  .card p{font-size:14px;line-height:20px;color:var(--muted);margin-left:12px;width:200px}

  /* contact */
  .contact-pink{left:520px;top:3060px;width:680px;height:828px;background:var(--pink)}
  .form-card{left:140px;top:3172px;width:512px;height:608px;background:var(--panel);box-shadow:0 0 0 16px var(--white),0 8px 24px rgba(0,0,0,.3);padding:32px 40px}
  .form-card h4{color:var(--white);font-size:16px;margin-bottom:24px}
  .field{background:var(--white);height:56px;margin-bottom:24px;font-size:13px;color:#888;padding:10px 14px}
  .field.msg{height:144px}
  .submit{position:absolute;right:64px;bottom:36px;background:var(--pink);color:var(--white);font-size:14px;padding:8px 18px}
  .brand-foot{left:780px;top:3076px}
  .brand-foot .brand-dot{background:var(--white)}
  .brand-foot .brand-name{color:var(--white)}
  .contact-text{left:780px;top:3192px;width:360px;color:var(--white);font-size:20px;line-height:32px;font-weight:700}
  .phones{left:780px;top:3368px;color:var(--white);font-size:22px;line-height:48px}
  .social{left:780px;top:3620px;display:flex;gap:40px}
  .social span{width:44px;height:44px;background:var(--white)}
</style>
</head>
<body>
  <!-- header / hero -->
  <div class="abs hero-bg placeholder" role="img" aria-label="Pale blue background with faint care-themed icon pattern"></div>
  <div class="abs brand"><span class="brand-dot"></span><span class="brand-name">Carelume</span></div>
  <nav class="abs nav">
    <a href="#">Home</a><a href="#">Services</a><a href="#">FAQ</a><a href="#">Contact Us</a><a href="#" class="login">Login</a>
  </nav>
  <h1 class="abs hero-title">Lorem ipsum dolor sit amet, consectetur</h1>
  <p class="abs hero-text">adipiscing elit, sed do eiusmod tempor incididunt ut labore et dolore magna aliqua. Quis ipsum</p>
  <a class="abs btn">Book a Demo</a>
  <div class="abs frame hero-photo">
    <div role="img" aria-label="Photo of a carer with an elderly woman in a wheelchair outdoors" style="width:100%;height:100%;background:linear-gradient(160deg,#8fb06a,#d9e0d6 55%,#6f8f9c)"></div>
  </div>

  <!-- features -->
  <div class="abs features-head"><h2>Our Features</h2></div>
  <div class="abs features-band"></div>
  <div class="abs frame features-photo">
    <div role="img" aria-label="Photo of a nurse in scrubs and an elderly man, both wearing masks" style="width:100%;height:100%;background:linear-gradient(135deg,#6fb3b8,#cfd3d1 50%,#7a6f66)"></div>
  </div>
  <ul class="abs feature-list">
    <li>Lorem ipsum dolor sit amet, consectetur</li>
    <li>Lorem ipsum dolor sit amet, consectetur</li>
    <li>Lorem ipsum dolor sit amet, consectetur</li>
    <li>Lorem ipsum dolor sit amet, consectetur</li>
    <li>Lorem ipsum dolor sit amet, consectetur</li>
    <li>Lorem ipsum dolor sit amet, consectetur</li>
  </ul>

  <!-- testimonial -->
  <div class="abs quote-band placeholder" role="img" aria-label="Dark photo of hands holding an elderly person's hand"></div>
  <p class="abs quote">“ Lorem ipsum dolor sit amet, consectetur adipiscing elit, sed do eiusmod tempor incididunt ut labore et dolore magna aliqua. Quis ipsum suspendisse ultrices gravida. Ri commodo viverra maecenas ”</p>
  <div class="abs dots"><span></span><span class="on"></span><span></span><span></span></div>

  <!-- services -->
  <div class="abs services-bg placeholder" role="img" aria-label="Pale blue background with faint care-themed icon pattern"></div>
  <div class="abs services-head"><h2>Our Services</h2></div>
  <article class="abs card" style="left:72px">
    <div class="card-photo" role="img" aria-label="Photo of a carer supporting an elderly person walking" style="background:linear-gradient(135deg,#6b5d55,#c9b8a8)"></div>
    <h3>Lorem ipsum</h3>
    <p>Lorem ipsum dolor sit amet, consectetur adipiscing elit, sed do eiusmod tempor incididunt ut labore et</p>
  </article>
  <article class="abs card" style="left:368px">
    <div class="card-photo" role="img" aria-label="Photo of medical staff with a stethoscope" style="background:linear-gradient(135deg,#3f6f7a,#b7cfd2)"></div>
    <h3>Lorem ipsum</h3>
    <p>Lorem ipsum dolor sit amet, consectetur adipiscing elit, sed do eiusmod tempor incididunt ut labore et</p>
  </article>
  <article class="abs card" style="left:652px">
    <div class="card-photo" role="img" aria-label="Photo of a carer with an elderly woman at home" style="background:linear-gradient(135deg,#d8c2a8,#f1e6da)"></div>
    <h3>Lorem ipsum</h3>
    <p>Lorem ipsum dolor sit amet, consectetur adipiscing elit, sed do eiusmod tempor incididunt ut labore et</p>
  </article>
  <article class="abs card" style="left:932px">
    <div class="card-photo" role="img" aria-label="Photo of a doctor in a white coat" style="background:linear-gradient(135deg,#e4e6e3,#8a9a9a)"></div>
    <h3>Lorem ipsum</h3>
    <p>Lorem ipsum dolor sit amet, consectetur adipiscing elit, sed do eiusmod tempor incididunt ut labore et</p>
  </article>

  <!-- contact -->
  <div class="abs contact-pink"></div>
  <form class="abs form-card">
    <h4>Any Queries?</h4>
    <div class="field">Name</div>
    <div class="field">E-mail</div>
    <div class="field">Subject</div>
    <div class="field msg">Message</div>
    <span class="submit">Submit</span>
  </form>
  <div class="abs brand brand-foot"><span class="brand-dot"></span><span class="brand-name">Carelume</span></div>
  <p class="abs contact-text">Lorem ipsum dolor sit amet, consectetur adipiscing elit, sed do eiusmod tempor incididunt ut labore et dolore magna aliqua. Quis</p>
  <p class="abs phones">123456765432<br>123456765432</p>
  <div class="abs social"><span></span><span></span><span></span><span></span></div>
</body>
</html>
```